Harbor Crest Solutions Letterhead Design

The project name sums it up. Just need a professional letterhead design / template we can use in our marketing folders.

Here's the address / contact info for the letterhead: Harbor Crest Solutions 4817 Maple Ridge Dr Suite 150 League City, Texas 77419 346-508-7364 www.harborcrestsolutions.us support@harborcrestsolutions.us

```html
<!DOCTYPE html>
<html lang="en">
<head>
<meta charset="utf-8">
<title>Harbor Crest Solutions Letterhead</title>
<link rel="stylesheet" href="https://fonts.googleapis.com/css2?family=Roboto:wght@400;700&display=swap">
<style>
  :root {
    --backdrop: #dcdcdc;
    --paper: #f8f8f8;
    --ink: #3b3b3b;
    --brand-ink: #111214;
    --accent-navy: #1d3a6b;
    --watermark: #ececec;
    --band-grey: #7b7d7e;
    --band-black: #0d0e10;
    --band-text: #ffffff;
  }
  * { margin: 0; padding: 0; box-sizing: border-box; }
  html, body {
    width: 1153px;
    height: 1200px;
    overflow: hidden;
    background: var(--backdrop);
    font-family: "Roboto", Arial, sans-serif;
  }
  .letterhead {
    position: absolute;
    left: 166px;
    top: 28px;
    width: 820px;
    height: 1144px;
    background: var(--paper);
    overflow: hidden;
  }
  .brand {
    position: absolute;
    left: 86px;
    top: 114px;
    display: flex;
    align-items: center;
    gap: 10px;
  }
  .brand-square {
    width: 22px;
    height: 22px;
    background: var(--brand-ink);
  }
  .brand-name {
    font-weight: 700;
    font-size: 24px;
    color: var(--brand-ink);
    letter-spacing: 0.2px;
  }
  .contact {
    position: absolute;
    left: 451px;
    top: 76px;
    font-size: 16px;
    line-height: 20px;
    color: var(--ink);
  }
  .contact-address { margin-bottom: 7px; }
  .contact-line {
    display: flex;
    align-items: center;
    gap: 5px;
    height: 21px;
  }
  .contact-line svg { flex: none; }
  .watermark-name {
    position: absolute;
    left: 0;
    right: 0;
    top: 520px;
    text-align: center;
    font-weight: 700;
    font-size: 54px;
    color: var(--watermark);
  }
  .footer-band {
    position: absolute;
    left: 0;
    bottom: 0;
    width: 820px;
    height: 30px;
  }
  .footer-url {
    position: absolute;
    left: 522px;
    bottom: 5px;
    font-size: 16px;
    color: var(--band-text);
    letter-spacing: 0.2px;
  }
</style>
</head>
<body>
  <main class="letterhead">
    <header>
      <div class="brand">
        <span class="brand-square"></span>
        <span class="brand-name">Harbor Crest Solutions</span>
      </div>
      <address class="contact" style="font-style: normal;">
        <div class="contact-address">4817 Maple Ridge Dr<br>Suite 150 League City, Texas 77419</div>
        <div class="contact-line">
          <svg width="16" height="16" viewBox="0 0 24 24" aria-hidden="true"><path fill="var(--accent-navy)" d="M6.6 10.8c1.4 2.8 3.8 5.1 6.6 6.6l2.2-2.2c.3-.3.7-.4 1-.2 1.1.4 2.3.6 3.6.6.6 0 1 .4 1 1V20c0 .6-.4 1-1 1C10.6 21 3 13.4 3 4c0-.6.4-1 1-1h3.5c.6 0 1 .4 1 1 0 1.3.2 2.5.6 3.6.1.3 0 .7-.2 1z"/></svg>
          <span>346-508-7364</span>
        </div>
        <div class="contact-line">
          <svg width="16" height="12" viewBox="0 0 16 12" aria-hidden="true"><rect x="0" y="0" width="16" height="12" fill="var(--accent-navy)"/><path d="M1 1l7 5.5L15 1" fill="none" stroke="#fff" stroke-width="1.2"/></svg>
          <span>support@harborcrestsolutions.us</span>
        </div>
      </address>
    </header>

    <div class="watermark-name" aria-hidden="true">Harbor Crest Solutions</div>

    <footer>
      <svg class="footer-band" viewBox="0 0 820 30" preserveAspectRatio="none" aria-hidden="true">
        <polygon points="0,0 478,0 470,30 0,30" fill="var(--band-grey)"/>
        <polygon points="499,0 820,0 820,30 478,30" fill="var(--band-black)"/>
      </svg>
      <div class="footer-url">www.harborcrestsolutions.us</div>
    </footer>
  </main>
</body>
</html>
```